Microblading website contest - Make it colorful

Beauty salon focusing on microblading need a better website template. Please make a 1 page site mobile optimized and nicer layout with better color formulation. Would love interactive images in the site. You can use stock images and if approve we can pay for it.
Current site:
tessawynkelpeony.com

Inspiration:
https://framqueue.net/shots/41877260-Microblading-HomePage
https://framqueue.net/shots/7914026-Lunetto-Microblading-Eyebrow-Beauty-Salon-Pagewright-Theme

Target Market(s)

women

Industry/Entity Type

beauty salon

Number of Pages Required

1 page

Font styles to use
Serif
Decorative
Script

Requirements
Nice to have
• As pretty as possible

```html
<!DOCTYPE html>
<html lang="en">
<head>
<meta charset="utf-8">
<title>Tessa Peony Brow Atelier – Microblading</title>
<link href="https://fonts.googleapis.com/css2?family=Playfair+Display:wght@400;700&family=Roboto:wght@400;500;700&display=swap" rel="stylesheet">
<style>
:root{
  --blush:#f2e0e1;
  --rose:#b9384f;
  --rose-deep:#8c1c35;
  --ink:#1c1c1c;
  --muted:#9a8a8c;
  --white:#ffffff;
  --black:#000000;
}
*{margin:0;padding:0;box-sizing:border-box}
html,body{width:1200px;height:4815px;overflow:hidden}
body{position:relative;background:var(--white);font-family:"Roboto",Arial,sans-serif;color:var(--ink)}
.abs{position:absolute}
.serif{font-family:"Playfair Display",Georgia,serif;font-weight:400}
.btn{position:absolute;display:flex;align-items:center;justify-content:center;background:linear-gradient(90deg,var(--rose),var(--rose-deep));color:var(--white);font-size:14px;font-weight:500;letter-spacing:.3px;text-transform:uppercase}
.band{position:absolute;left:0;width:1200px}
.blush{background:var(--blush)}

/* header */
.logo{left:112px;top:22px;font-size:21px;font-weight:500;color:var(--rose);letter-spacing:.2px}
.nav{left:409px;top:28px;display:flex}
.nav a{font-size:12px;color:var(--ink);text-decoration:none;text-transform:uppercase;margin-right:32px}
.contact-btn{left:956px;top:14px;width:129px;height:43px;font-size:12px}

/* side markers */
.marker{position:absolute;left:30px;width:40px;text-align:center}
.marker .num{font-family:"Playfair Display",Georgia,serif;font-size:34px;color:#b8a7a9;line-height:1}
.marker .line{width:1px;height:110px;background:#c8b8ba;margin:14px auto 0}
.marker .label{margin:16px auto 0;writing-mode:vertical-rl;transform:rotate(180deg);font-size:10px;color:var(--muted);text-transform:uppercase;letter-spacing:.5px;white-space:nowrap}

/* hero */
.hero-frame{left:140px;top:150px;width:440px;height:504px;background:linear-gradient(160deg,#c64a5f,#a3243e)}
.hero-photo{left:170px;top:100px;width:420px;height:554px;background:linear-gradient(180deg,#3a2a26 0%,#d9b9a6 30%,#f4f1f0 70%,#ffffff 100%);border-radius:200px 200px 0 0;opacity:.9}
.hero-brush{left:598px;top:184px;width:418px;height:76px;background:var(--white);border-radius:40px;opacity:.85}
.hero-kicker{left:632px;top:196px;font-size:46px;color:var(--rose);letter-spacing:1px}
.hero-title{left:632px;top:288px;font-size:56px;line-height:1.12;color:var(--ink)}
.hero-sub{left:632px;top:444px;font-size:21px}
.hero-btn{left:632px;top:506px;width:150px;height:47px}

/* academy */
.collage{position:absolute}
.acad-h{left:608px;top:748px;font-size:46px}
.acad-kick{left:608px;top:812px;font-size:12px}
.acad-title{left:608px;top:840px;font-size:38px;line-height:1.18;width:520px}
.acad-place{left:608px;top:988px;font-size:17px}
.acad-body{left:608px;top:1030px;font-size:14px;line-height:1.6;width:450px}
.acad-btn{left:609px;top:1121px;width:154px;height:49px}

/* services */
.sec-title{width:1200px;left:0;text-align:center;font-size:44px}
.grid{left:112px;top:1465px;width:972px;height:488px;display:grid;grid-template-columns:repeat(4,243px);grid-template-rows:repeat(2,244px)}
.tile{position:relative;display:flex;align-items:flex-end;justify-content:center;padding-bottom:18px;text-align:center;font-family:"Playfair Display",Georgia,serif;color:var(--white);font-size:17px;line-height:1.15;text-transform:uppercase}
.tile.feature{background:var(--rose);align-items:flex-start;justify-content:flex-start;flex-direction:column;padding:60px 0 0 26px;text-align:left}
.tile.feature h3{font-family:"Playfair Display",Georgia,serif;font-weight:400;font-size:30px;margin-bottom:16px}
.tile.feature li{font-family:"Roboto",Arial,sans-serif;font-size:11px;font-weight:700;list-style:none;margin-bottom:9px}
.tile.feature li::before{content:"● ";font-size:8px}
.tile.feature p{font-family:"Roboto",Arial,sans-serif;font-size:14px;font-weight:700;margin:6px 0 0 16px}
.svc-btn{left:521px;top:2009px;width:186px;height:47px}

/* about */
.about-h{left:112px;top:2204px;font-size:46px}
.about-body{left:112px;top:2272px;width:420px;font-size:11.5px;line-height:1.7}
.about-body p{margin-bottom:14px}
.about-btn{left:112px;top:2548px;width:183px;height:48px}
.about-frame{left:609px;top:2172px;width:479px;height:454px;background:linear-gradient(180deg,var(--rose),var(--rose-deep))}
.about-photo{left:591px;top:2190px;width:478px;height:438px;background:linear-gradient(160deg,#f0ebe6,#cfc4bc 55%,#3b3233)}

/* gallery */
.gallery{top:2697px;height:664px;background:linear-gradient(180deg,#c64d60,#8d1f37)}
.gal-title{color:var(--white)}
.ph{position:absolute}

/* feedback */
.fb-frame{left:364px;top:3545px;width:464px;height:404px;border:3px solid var(--rose)}
.fb-sides{left:364px;top:3610px;width:464px;height:260px;background:var(--white)}
.avatar{left:540px;top:3489px;width:124px;height:124px;border-radius:50%;background:radial-gradient(circle at 45% 40%,#e2c2b4,#b58a7c)}
.fb-date{left:0;width:1200px;top:3622px;text-align:center;font-size:22px;font-weight:500}
.fb-text{left:300px;width:600px;top:3664px;text-align:center;font-size:23px;line-height:37.5px;white-space:nowrap}
.stars{left:534px;top:3893px}
.dots{left:573px;top:3968px;display:flex;gap:9px}
.dots span{width:10px;height:10px;border-radius:50%;background:#bdbdbd}
.dots span:first-child{background:var(--black)}

/* contact */
.map{left:112px;top:4108px;width:477px;height:352px;background:linear-gradient(135deg,#eceef0,#dfe6ea 60%,#b7d3e6)}
.form{left:609px;top:4108px;width:477px;height:352px;background:var(--white)}
.form h2{position:absolute;left:0;top:30px;width:100%;text-align:center;font-size:40px;color:var(--rose)}
.field{position:absolute;left:23px;width:430px;height:30px;border:1px solid #bbb;font-size:10px;padding:8px 10px;color:#444}
.form-btn{left:632px;top:4390px;width:134px;height:46px}

/* footer */
.footer{top:4529px;height:286px;background:var(--black);color:var(--white)}
.f-col{position:absolute;top:72px}
.f-col h4{font-size:19px;font-weight:500;margin-bottom:14px}
.f-col .brand{color:var(--rose)}
.f-col p,.f-col li{font-size:11px;line-height:1.9;list-style:none}
.f-row{display:flex;gap:10px;align-items:flex-start;margin-bottom:10px;font-size:11px;line-height:1.5}
.f-row i{flex:none;width:16px;height:16px;border-radius:50%;background:var(--white);display:block;margin-top:2px}
.copy{position:absolute;top:258px;width:1200px;text-align:center;font-size:11px}
</style>
</head>
<body>

<!-- Hero band -->
<section class="band blush" style="top:0;height:654px"></section>
<div class="abs logo">TESSAWYNKELPEONY</div>
<nav class="abs nav"><a>Home</a><a>About us</a><a>Services</a><a>Gallery</a><a>Shop</a><a>Academy</a></nav>
<div class="btn contact-btn">Contact us</div>

<div class="marker" style="top:256px"><div class="num">01</div><div class="line"></div><div class="label">Introduce</div></div>
<div class="abs hero-frame"></div>
<div class="abs hero-photo" role="img" aria-label="Portrait of the brow specialist in a white top"></div>
<div class="abs hero-brush"></div>
<div class="abs hero-kicker serif">MICROBLADING</div>
<h1 class="abs hero-title serif">PEONY BROWS<br>TESSA</h1>
<div class="abs hero-sub">Your personal eyebrow specialist</div>
<div class="btn hero-btn">Get started</div>

<!-- Academy -->
<div class="marker" style="top:842px"><div class="num">02</div><div class="line"></div><div class="label">Academy</div></div>
<div class="collage" role="img" aria-label="Students practising brow technique in class" style="left:323px;top:720px;width:208px;height:136px;background:linear-gradient(135deg,#d8d4d0,#6d625f)"></div>
<div class="collage" role="img" aria-label="Micro-needling course poster with master technician" style="left:202px;top:863px;width:280px;height:270px;background:linear-gradient(135deg,#7dbfc9,#e8eef0 55%,#8fa7ad);border:4px solid var(--white)"></div>
<div class="collage" role="img" aria-label="Graduates holding course certificates" style="left:303px;top:1077px;width:228px;height:149px;background:linear-gradient(135deg,#cfc8c2,#2e2a2a)"></div>
<h2 class="abs acad-h serif">ACADEMY</h2>
<div class="abs acad-kick">The most worthwhile investment is often yourself</div>
<div class="abs acad-title serif">International institution Lumeray European Skin Management Course</div>
<div class="abs acad-place">Wrenfield Harbor – Welcome to join us!</div>
<div class="abs acad-body">Small class, maximum 5 students each.<br>Full micro-needling technique. 1 to 1 course personally held by<br>Master technician Tessa</div>
<div class="btn acad-btn">Join now</div>

<!-- Services -->
<section class="band blush" style="top:1295px;height:813px"></section>
<div class="marker" style="top:1617px"><div class="num">03</div><div class="line"></div><div class="label">Services</div></div>
<h2 class="abs sec-title serif" style="top:1348px">OUR SERVICES</h2>
<div class="abs grid">
  <div class="tile" role="img" aria-label="Close-up of natural brows" style="background:linear-gradient(180deg,#cda995,#6e4c40)">Natural brows</div>
  <div class="tile feature"><h3>HAIR STROKE</h3><ul><li>TRENDY</li><li>MACHINE-DRAW LINE</li><li>NO WOUNDS</li></ul><p>FOR OILY SKIN TYPE</p></div>
  <div class="tile" role="img" aria-label="Technician shaping powder brows" style="background:linear-gradient(180deg,#3d3535,#9c7c70)">Powder brows</div>
  <div class="tile" role="img" aria-label="Brow pencil drawing a powder brow" style="background:linear-gradient(180deg,#a8603f,#6a3326)">Natural powder<br>brows (hand-draw<br>powder)</div>
  <div class="tile" role="img" aria-label="Close-up of eye with inner eyeliner" style="background:linear-gradient(180deg,#c7c9c8,#3a3433)">Natural eyeliner<br>(inner eyelid)</div>
  <div class="tile" role="img" aria-label="Eyeliner being applied to closed eye" style="background:linear-gradient(180deg,#e3b395,#7a4a39)">Makeup eyeliner</div>
  <div class="tile" role="img" aria-label="Artist applying powder eyeliner" style="background:linear-gradient(180deg,#caa590,#6c4335)">Powder eyeliner<br>(natural eyeshadow)</div>
  <div class="tile" role="img" aria-label="Scalp micropigmentation treatment" style="background:linear-gradient(180deg,#d9d4d1,#4d4444)">Scalp<br>micropigmentation</div>
</div>
<div class="btn svc-btn">View all services</div>

<!-- About -->
<div class="marker" style="top:2318px"><div class="num">04</div><div class="line"></div><div class="label">About us</div></div>
<h2 class="abs about-h serif">ABOUT&nbsp; TESSA</h2>
<div class="abs about-body">
  <p>Tessa has 7 years of microblading experience. She graduated from VelaTouch United States. After, she studied in Quillacademy, a global top brand from Germany. She was personally guided by the brand CEO Dario Vukan and the first China Master Mei Sorel.</p>
  <p>After earning award of Lumebrows Artist in 2019, Tessa continued her practice microblading until she won the world's first Lumebrows Master in Taiwan in 2021. She is currently the only certificated Master technician in Taiwan. She also holds a shading and Lumeray Master.</p>
  <p>On Tessa's microblading journey. She travelled to places all over the world and met mentors on her path. She was willing to learn any new tech and inspire a better self regardless how much the cost was.</p>
</div>
<div class="btn about-btn">Learn more</div>
<div class="abs about-frame"></div>
<div class="abs about-photo" role="img" aria-label="Tessa with graduates holding certificates in front of a banner"></div>

<!-- Gallery -->
<section class="band gallery"></section>
<div class="marker" style="top:2965px"><div class="num" style="color:#e7b8c0">05</div><div class="line" style="background:#e7b8c0"></div><div class="label" style="color:#f0ccd2">Photo gallery</div></div>
<h2 class="abs sec-title serif gal-title" style="top:2752px">PHOTO GALLERY</h2>
<div class="ph" role="img" aria-label="Before and after brow results" style="left:112px;top:2848px;width:477px;height:430px;background:linear-gradient(90deg,#d7b6a3,#efd9cc 50%,#d4b09c)"></div>
<div class="ph" role="img" aria-label="Technician working under ring light" style="left:613px;top:2848px;width:226px;height:206px;background:linear-gradient(135deg,#e9e2dc,#5c514e)"></div>
<div class="ph" role="img" aria-label="Masked technician at work" style="left:860px;top:2848px;width:228px;height:206px;background:linear-gradient(135deg,#d6c7bd,#3b3333)"></div>
<div class="ph" role="img" aria-label="Treatment room with client on bed" style="left:613px;top:3075px;width:226px;height:205px;background:linear-gradient(135deg,#cdb9a3,#6a5747)"></div>
<div class="ph" role="img" aria-label="Training session with presentation screen" style="left:860px;top:3075px;width:228px;height:205px;background:linear-gradient(135deg,#f1ede8,#8d7f79)"></div>

<!-- Feedback -->
<div class="marker" style="top:3621px"><div class="num">06</div><div class="line"></div><div class="label">Customer feedback</div></div>
<h2 class="abs sec-title serif" style="top:3406px">CUSTOMER FEEDBACK</h2>
<div class="abs fb-frame"></div>
<div class="abs fb-sides"></div>
<div class="abs avatar" role="img" aria-label="Close-up of treated skin"></div>
<div class="abs fb-date">02 .13 .2020</div>
<p class="abs fb-text">It was my first time doing the whole face<br>micro-needling treatment at Tessa's place and I am<br>absolutelyin love with it. I can see the darkness of<br>my scars hasimproved and the skin has changed<br>smooth as well! Definitely recommend people to get<br>the package as well, good deal to save $!</p>
<svg class="abs stars" width="132" height="24" viewBox="0 0 132 24">
  <g fill="#e6b400">
    <polygon points="12,1 15,9 23,9 17,14 19,23 12,18 5,23 7,14 1,9 9,9"/>
    <polygon transform="translate(27 0)" points="12,1 15,9 23,9 17,14 19,23 12,18 5,23 7,14 1,9 9,9"/>
    <polygon transform="translate(54 0)" points="12,1 15,9 23,9 17,14 19,23 12,18 5,23 7,14 1,9 9,9"/>
    <polygon transform="translate(81 0)" points="12,1 15,9 23,9 17,14 19,23 12,18 5,23 7,14 1,9 9,9"/>
    <polygon transform="translate(108 0)" points="12,1 15,9 23,9 17,14 19,23 12,18 5,23 7,14 1,9 9,9"/>
  </g>
</svg>
<div class="abs dots"><span></span><span></span><span></span></div>

<!-- Contact -->
<section class="band blush" style="top:4034px;height:495px"></section>
<div class="marker" style="top:4212px"><div class="num">07</div><div class="line"></div><div class="label">Contact</div></div>
<div class="abs map" role="img" aria-label="Street map around the studio in Wrenfield"></div>
<svg class="abs" style="left:290px;top:4260px" width="20" height="28" viewBox="0 0 20 28"><path d="M10 0C4.5 0 0 4.4 0 9.8 0 17 10 28 10 28s10-11 10-18.2C20 4.4 15.5 0 10 0z" fill="#d63a2f"/><circle cx="10" cy="10" r="4" fill="#fff"/></svg>
<div class="abs form">
  <h2 class="serif">GET IN TOUCH</h2>
  <div class="field" style="top:102px">Name :</div>
  <div class="field" style="top:141px">Address :</div>
  <div class="field" style="top:180px">Email :</div>
  <div class="field" style="top:220px;height:68px">Message :</div>
</div>
<div class="btn form-btn">Book now</div>

<!-- Footer -->
<footer class="band footer">
  <div class="f-col" style="left:112px;width:250px">
    <h4 class="brand">TESSAWYNKELPEONY</h4>
    <p>Lorem ipsum dolor sit amet, consectetur adipiscing elit, sed do eiusmod tempor incididunt ut labore et dolore magna aliqua. Quis ipsum suspendisse ultrices gravida. Risus commodo viverra maecenas accumsan lacus vel facilisis.</p>
  </div>
  <div class="f-col" style="left:426px">
    <h4>MENU</h4>
    <ul><li>Home</li><li>About us</li><li>Services</li><li>Gallery</li><li>Shop</li><li>Academy</li></ul>
  </div>
  <div class="f-col" style="left:622px;width:300px">
    <h4>CONTACT US</h4>
    <div class="f-row"><i></i><span>Tessa Peony Brow Atelier<br>27-40 Harlow Ave, Wrenfield, WH 40512</span></div>
    <div class="f-row"><i></i><span>hello@tessawynkelpeony.com</span></div>
    <div class="f-row"><i></i><span>Opening hours:<br>Monday to Sunday 11:00-18:00<br>We only take reservations, no walk in</span></div>
  </div>
  <div class="f-col" style="left:944px">
    <h4>FOLLOW US</h4>
    <div class="f-row"><i></i><span>Facelink</span></div>
    <div class="f-row"><i></i><span>Chirper</span></div>
    <div class="f-row"><i></i><span>Viewtube</span></div>
    <div class="f-row"><i></i><span>Snapgram</span></div>
  </div>
  <div class="copy">This website is created by TessaPeonyBrows &nbsp;|&nbsp; Copyright 2015</div>
</footer>

</body>
</html>
```